Corvane Property Group Business cards

I am starting a property development and consultancy business called Corvane Property Group. I have a logo designed and a website on its way:
www.corvanegroup-example.com.au

I need a business card with the following:

Front:
Mostly orange with logo taking up all front of card

Back of card:
Logo

Mark Dellaway
Managing Director

T +61 452 907 364
E mark.dellaway@corvanegroup-example.com.au
www.corvanegroup-example.com.au

Industry/Entity Type

Business

Requirements
Must have
• curved edges

```html
<!DOCTYPE html>
<html lang="en">
<head>
<meta charset="utf-8">
<title>Corvane Property Group – Business Cards</title>
<link rel="stylesheet" href="https://fonts.googleapis.com/css2?family=Open+Sans:wght@400;600&display=swap">
<style>
  :root {
    --orange: #efa212;
    --orange-deep: #e4960a;
    --paper: #ffffff;
    --ink: #2b2b2b;
    --ink-soft: #3a3a3a;
    --backdrop: #d9d9d9;
  }
  * { box-sizing: border-box; margin: 0; padding: 0; }
  html, body {
    width: 1200px; height: 900px; overflow: hidden;
    background: var(--backdrop);
    font-family: "Open Sans", Arial, sans-serif;
  }
  .sheet { position: relative; width: 1200px; height: 900px; }
  .card {
    position: absolute; left: 290px; width: 620px; height: 378px;
    border-radius: 26px;
    box-shadow: 0 8px 24px rgba(0,0,0,0.18);
    overflow: hidden;
  }
  .card--front {
    top: 52px;
    background: linear-gradient(135deg, var(--orange-deep), var(--orange));
  }
  .card--back { top: 468px; background: var(--paper); }

  .front-name {
    position: absolute; left: 56px; top: 100px;
    color: var(--paper); font-weight: 400;
    line-height: 1; white-space: nowrap;
  }
  .front-name .line-main { display: block; font-size: 100px; letter-spacing: 2px; }
  .front-name .line-sub { display: block; font-size: 36px; letter-spacing: 8px; margin-top: 12px; color: var(--ink); }

  .back-brand {
    position: absolute; left: 40px; top: 34px;
    display: flex; align-items: flex-start; gap: 14px;
    color: var(--orange); font-weight: 400; line-height: 1; white-space: nowrap;
  }
  .back-brand .mark-square { width: 22px; height: 22px; background: var(--orange); margin-top: 14px; }
  .back-brand .line-main { display: block; font-size: 58px; letter-spacing: 3px; }
  .back-brand .line-sub { display: block; font-size: 20px; letter-spacing: 5.5px; margin-top: 6px; color: var(--ink); }

  .person {
    position: absolute; left: 28px; top: 222px; width: 206px; text-align: right;
    white-space: nowrap;
  }
  .person-name { font-size: 28px; font-weight: 400; color: var(--ink); }
  .person-title { font-size: 14px; letter-spacing: 0.5px; color: var(--ink-soft); margin-top: 2px; }

  .divider {
    position: absolute; left: 250px; top: 228px; width: 2px; height: 110px;
    background: var(--orange);
  }
  .contact {
    position: absolute; left: 268px; top: 240px;
    font-size: 13px; color: var(--ink); line-height: 1.6; white-space: nowrap;
  }
  .contact .label { font-weight: 600; margin-right: 4px; }
  .contact .web { color: var(--orange); margin-top: 14px; font-size: 14px; }
</style>
</head>
<body>
<main class="sheet">
  <section class="card card--front" aria-label="Card front">
    <div class="front-name">
      <span class="line-main">CORVANE</span>
      <span class="line-sub">PROPERTY GROUP</span>
    </div>
  </section>

  <section class="card card--back" aria-label="Card back">
    <div class="back-brand">
      <div class="mark-square"></div>
      <div>
        <span class="line-main">CORVANE</span>
        <span class="line-sub">PROPERTY GROUP</span>
      </div>
    </div>

    <div class="person">
      <p class="person-name">Mark Dellaway</p>
      <p class="person-title">MANAGING DIRECTOR</p>
    </div>

    <div class="divider"></div>

    <div class="contact">
      <p><span class="label">T:</span>+61 452 907 364</p>
      <p><span class="label">E:</span>mark.dellaway@corvanegroup-example.com.au</p>
      <p class="web">www.corvanegroup-example.com.au</p>
    </div>
  </section>
</main>
</body>
</html>
```